Business Card Design Project

I need a new business card design for my building/development company: Kestrel Ridge Builders.

We specialise in small sub-divisions, multi-story developments and new house builds.
We handle the whole process from concept stage right throught to a fully developed property.
Updates

Target Market(s)

people looking to develop their property and need help. New property buyers

Industry/Entity Type

House

Requirements
Must have
• My logo on both sides:
Side 1: Logo taking up whole side as per old card but with a color/style change.

Side 2: Contact page: include logo but the rest just surprise me!

All contact details will be: (and need to be changable for each employee) I'll inform you of specifics before printing.

Name Surname
Position ie. Managing director
M: insert mobile
E: insert email
P.O. Box 518, Ashwell, Vic, 3094
www.kestrelridgebuilders.com.au

Nice to have
• Colors i'd like: (not necessarily all but this is the basic idea)

Black, blue, grey, silver, white

```html
<!DOCTYPE html>
<html lang="en">
<head>
<meta charset="utf-8">
<title>Kestrel Ridge Builders – Business Cards</title>
<link rel="stylesheet" href="https://fonts.googleapis.com/css2?family=Open+Sans:wght@400;600;700&display=swap">
<style>
  :root {
    --canvas: #e6e6e4;
    --card-dark: #2e2f32;
    --card-dark-edge: #3b3c40;
    --card-light: #f1f1f1;
    --card-light-edge: #e2e3e4;
    --blue: #1b82c5;
    --ink: #1f2022;
    --silver: #d6d7d9;
    --muted: #a9abae;
  }
  * { margin: 0; padding: 0; box-sizing: border-box; }
  html, body { width: 1200px; height: 880px; overflow: hidden; }
  body {
    background: var(--canvas);
    font-family: "Open Sans", Arial, sans-serif;
    position: relative;
  }
  .card {
    position: absolute;
    top: 281px;
    width: 520px;
    height: 318px;
    overflow: hidden;
    box-shadow: 0 10px 28px rgba(0,0,0,0.22);
  }

  /* Front: dark logo side */
  .card--front {
    left: 40px;
    background: linear-gradient(135deg, var(--card-dark) 0%, var(--card-dark-edge) 100%);
    color: var(--silver);
  }
  .front-lockup {
    position: absolute;
    left: 0; right: 0; top: 96px;
    display: flex;
    flex-direction: column;
    align-items: center;
  }
  .brand-row { display: flex; align-items: center; gap: 14px; }
  .brand-mark { width: 26px; height: 26px; background: var(--blue); }
  .front-name {
    font-size: 34px;
    font-weight: 600;
    color: var(--silver);
    letter-spacing: 0.2px;
  }
  .front-tagline {
    margin-top: 6px;
    font-size: 17px;
    letter-spacing: 0.6px;
    color: var(--silver);
  }
  .front-web {
    position: absolute;
    left: 0; right: 0; bottom: 36px;
    text-align: center;
    font-size: 15px;
    letter-spacing: 1.2px;
    color: var(--muted);
  }

  /* Back: contact side */
  .card--back {
    left: 640px;
    background: linear-gradient(160deg, #ffffff 0%, var(--card-light) 60%, var(--card-light-edge) 100%);
    color: var(--ink);
  }
  .back-lockup {
    position: absolute;
    left: 24px; top: 96px;
    width: 190px;
  }
  .back-name {
    font-size: 19px;
    font-weight: 700;
    line-height: 1.15;
    color: var(--blue);
  }
  .back-tagline {
    margin-top: 6px;
    font-size: 9.5px;
    color: var(--ink);
    letter-spacing: 0.2px;
  }
  .divider {
    position: absolute;
    left: 226px; top: 52px;
    width: 1px; height: 160px;
    background: #9a9c9f;
  }
  .person {
    position: absolute;
    right: 32px; top: 92px;
    text-align: right;
  }
  .person-name { font-size: 18px; font-weight: 700; color: var(--ink); }
  .person-role { font-size: 15px; color: var(--blue); margin-top: 2px; }
  .role-tab {
    position: absolute;
    right: 0; top: 116px;
    width: 9px; height: 30px;
    background: var(--blue);
    border-radius: 4px 0 0 4px;
  }
  .contacts {
    position: absolute;
    left: 244px; top: 140px;
    list-style: none;
    font-size: 13px;
    line-height: 1.3;
  }
  .contacts li { display: flex; align-items: center; gap: 8px; margin-bottom: 6px; }
  .contacts .plain { padding-left: 22px; margin-top: -4px; }
  .contacts svg { width: 14px; height: 14px; flex: none; fill: var(--blue); }
  .band-dark {
    position: absolute;
    left: 0; bottom: 0;
    width: 360px; height: 14px;
    background: var(--card-dark);
  }
  .band-blue {
    position: absolute;
    right: 0; bottom: 0;
    width: 172px; height: 9px;
    background: var(--blue);
    clip-path: polygon(8px 0, 100% 0, 100% 100%, 0 100%);
  }
</style>
</head>
<body>

  <section class="card card--front" aria-label="Business card front">
    <div class="front-lockup">
      <div class="brand-row">
        <span class="brand-mark"></span>
        <span class="front-name">Kestrel Ridge Builders</span>
      </div>
      <p class="front-tagline">renovation-construction-development</p>
    </div>
    <p class="front-web">www.kestrelridgebuilders.com.au</p>
  </section>

  <section class="card card--back" aria-label="Business card back">
    <div class="back-lockup">
      <p class="back-name">Kestrel Ridge Builders</p>
      <p class="back-tagline">renovation-construction-development</p>
    </div>
    <span class="divider"></span>

    <div class="person">
      <p class="person-name">Name Surname</p>
      <p class="person-role">Managing director</p>
    </div>
    <span class="role-tab"></span>

    <ul class="contacts">
      <li>
        <svg viewBox="0 0 16 16" aria-hidden="true"><rect x="4" y="1" width="8" height="14" rx="1.5"/><rect x="5.5" y="3" width="5" height="7" fill="#fff"/></svg>
        <span>0412 555 209</span>
      </li>
      <li>
        <svg viewBox="0 0 16 16" aria-hidden="true"><rect x="1" y="3" width="14" height="10" rx="1"/><path d="M1.5 3.5 8 9l6.5-5.5" fill="none" stroke="#fff" stroke-width="1.4"/></svg>
        <span>name@kestrelridgebuilders.com.au</span>
      </li>
      <li>
        <svg viewBox="0 0 16 16" aria-hidden="true"><path d="M8 1 1 7.5h2V15h4v-4h2v4h4V7.5h2z"/></svg>
        <span>P.O. Box 518, Ashwell, Vic, 3094</span>
      </li>
      <li>
        <svg viewBox="0 0 16 16" aria-hidden="true"><circle cx="8" cy="8" r="7"/><path d="M1 8h14M8 1c-3 3-3 11 0 14M8 1c3 3 3 11 0 14" fill="none" stroke="#fff" stroke-width="1"/></svg>
        <span>www.kestrelridgebuilders.com.au</span>
      </li>
    </ul>

    <span class="band-dark"></span>
    <span class="band-blue"></span>
  </section>

</body>
</html>
```